Professional Business Cards

We need a nice looking, profession and modern business card for our new company. Our logo is attatched

Target Market(s)

Young Professionals

Industry/Entity Type

Financial

Contact Information for Business Card

FRONT

Morvane Tally Pty Ltd
Level 22, Halden Court, 48 Wirrapool St
Sydney NSW 2000
ABN : 57 304 918 226

Derek Wallis - Chief Operations Officer
P : 02 7153 2819
M: 0418 395 207
derek@morvanetally,com

BACK

- Cryptocurrency Exchange Services
- Cryptocurrency Mining Operations
- Cryptocurrency Investment Fund Offering

Font styles to use
Sans Serif

Colors
0255a3
9d9d9d

```html
<!DOCTYPE html>
<html lang="en">
<head>
<meta charset="utf-8">
<title>Morvane Tally — Business Cards</title>
<link href="https://fonts.googleapis.com/css2?family=Questrial&display=swap" rel="stylesheet">
<style>
  :root {
    --brand-blue: #0255a3;
    --brand-grey: #9d9d9d;
    --chevron-grey: #6b6c6e;
    --ink: #4a4a4a;
    --paper-light: #ffffff;
    --paper-shade: #e6e6e6;
    --backdrop: #2b2b2d;
  }
  * { box-sizing: border-box; margin: 0; padding: 0; }
  html, body {
    width: 1200px; height: 834px; overflow: hidden;
    background: var(--backdrop);
    font-family: "Questrial", "Century Gothic", sans-serif;
  }
  .stage {
    width: 1200px; height: 834px;
    display: flex; align-items: center; justify-content: center; gap: 40px;
  }
  .card {
    position: relative;
    width: 540px; height: 330px;
    background: linear-gradient(135deg, var(--paper-light) 0%, var(--paper-shade) 100%);
    overflow: hidden;
    box-shadow: 0 10px 30px rgba(0,0,0,.45);
  }
  .wordmark {
    display: flex; align-items: center; gap: 10px;
    color: var(--brand-blue);
  }
  .wordmark-square {
    width: 26px; height: 26px; background: var(--brand-blue);
  }
  .wordmark-name {
    font-size: 30px; letter-spacing: 1px; text-transform: uppercase;
    color: var(--brand-blue); white-space: nowrap;
  }

  /* Back card */
  .card-back .chevron { position: absolute; inset: 0; width: 100%; height: 100%; }
  .card-back .wordmark { position: absolute; left: 66px; top: 120px; }
  .services {
    position: absolute; left: 18px; top: 190px; width: 384px;
    text-align: center; color: var(--ink); font-size: 11px; line-height: 1.6;
    white-space: nowrap;
  }

  /* Front card */
  .card-front .person { position: absolute; right: 40px; top: 44px; text-align: left; }
  .person-name { font-size: 19px; font-weight: 700; color: var(--ink); }
  .person-title { font-size: 14px; color: var(--brand-blue); }
  .card-front .wordmark { position: absolute; left: 50px; top: 100px; }
  .band {
    position: absolute; left: 0; right: 0; top: 150px; height: 105px;
    background: linear-gradient(90deg, #1a63ad 0%, var(--brand-blue) 100%);
  }
  .address {
    position: absolute; left: 50px; top: 162px;
    color: #fff; font-size: 13px; line-height: 1.45; font-style: normal;
  }
  .address-company { font-weight: 700; }
  .contacts {
    position: absolute; left: 50px; top: 266px;
    font-size: 13.5px; line-height: 1.4; color: var(--ink);
    display: grid; grid-template-columns: 22px auto;
  }
  .contact-label { color: var(--brand-blue); font-weight: 700; }
</style>
</head>
<body>
<main class="stage">
  <section class="card card-back" aria-label="Business card back">
    <svg class="chevron" viewBox="0 0 540 330" aria-hidden="true">
      <polygon points="445,0 540,0 540,330 410,185" fill="var(--brand-blue)"/>
      <polygon points="478,0 540,0 540,225 455,125" fill="var(--chevron-grey)"/>
      <polygon points="508,0 540,0 540,110 500,62" fill="var(--paper-light)"/>
    </svg>
    <div class="wordmark">
      <span class="wordmark-square"></span>
      <span class="wordmark-name">Morvane Tally</span>
    </div>
    <p class="services">
      Cryptocurrency Exchange Services &nbsp;|&nbsp; Cryptocurrency Mining Operations<br>
      Cryptocurrency Investment Fund Offering
    </p>
  </section>

  <section class="card card-front" aria-label="Business card front">
    <div class="person">
      <p class="person-name">Derek Wallis</p>
      <p class="person-title">Chief Operations Officer</p>
    </div>
    <div class="wordmark">
      <span class="wordmark-square"></span>
      <span class="wordmark-name">Morvane Tally</span>
    </div>
    <div class="band"></div>
    <address class="address">
      <p class="address-company">Morvane Tally Pty Ltd</p>
      <p>Level 22, Halden Court, 48 Wirrapool St</p>
      <p>Sydney NSW 2000</p>
      <p>ABN : 57 304 918 226</p>
    </address>
    <div class="contacts">
      <span class="contact-label">P</span><span>02 7153 2819</span>
      <span class="contact-label">M</span><span>0418 395 207</span>
      <span class="contact-label">E</span><span>derek@morvanetally.com</span>
    </div>
  </section>
</main>
</body>
</html>
```